Flyer-Design für Vermietung und Verkauf von Palettenmöbeln
Zielgruppe
Ich vermiete und verkaufe in Tischler-Handarbeit hergestellte Palettenmöbel aus recycelten Paletten, wobei mein Schwerpunkt bei der Vermietung liegt. Meine Zielgruppe sind alle, die Veranstaltungen, Events , Messen, Präsentationen, private Feiern und Ähnliches planen und organisieren. Große und kleine Firmen, senatseigene Stellen, Privatpersonen, aber der Schwerpunkt liegt bei den Eventagenturen, welche mit der Organisation verschiedenster Veranstaltungen beauftragt werden.
Aufgabenstellung
Ich hätte ein klares und modernes Design mit BÄHM-Charakter. Der Flyer soll ein Hingucker sein, aber den Betrachter nicht erschlagen. Das Thema Nachhaltigkeit (die Möbel sind aus recylten Paletten) sollte bedacht werden. Ich hätte gern einen Faltflyer in DIN lang Größe. Dies ist für einen Mailing-Versand besser geeignet. Ich liefere eigene Bilder, aber sollten ein Stock-Bilder hilfreich sein, können dies gern verwendet werden. Ich habe natürlich noch mehr Bilder und kann diese gern zur Verfügung stellen, wenn ich weiß was benötigt wird. Es soll nicht viel Text in den Flyer. Ich bin hier sehr dankbar für Vorschläge, da ich mich mit dem Text sehr schwer tue. Ich hoffe, die Profis können mir auch beim Text helfen. Ich stelle auch Fotos meines alten Flyer zur Verfügung. Dieser ist definitv zu konservativ, langweilig und veraltet. Ich brauche ein modernes, hippes Design mit überzeugendem Text.

```html
<!DOCTYPE html>
<html lang="de">
<head>
<meta charset="utf-8">
<title>Holzlounge – Palettenmöbel Flyer</title>
<link rel="stylesheet" href="https://fonts.googleapis.com/css2?family=Lora:wght@400;700&family=Playfair+Display:ital,wght@1,900&display=swap">
<style>
  :root {
    --forest: #4f5b47;
    --sage: #d1e0c9;
    --ink-green: #2c3b22;
    --ink: #333330;
    --paper: #ffffff;
    --photo-warm-a: #e86a2c;
    --photo-warm-b: #a8452a;
    --photo-warm-c: #d0338a;
    --photo-cool-a: #8f3fc0;
    --photo-cool-b: #c85a8e;
    --photo-cool-c: #b88a7a;
  }
  * { margin: 0; padding: 0; box-sizing: border-box; }
  html, body { width: 1200px; height: 927px; overflow: hidden; background: var(--paper); }
  .flyer {
    position: relative;
    width: 1200px;
    height: 927px;
    overflow: hidden;
    background: var(--forest);
    font-family: "Lora", Georgia, serif;
    color: var(--ink);
  }
  .display { font-family: "Playfair Display", Georgia, serif; font-style: italic; font-weight: 900; color: var(--ink-green); }

  /* left column */
  .side-panel { position: absolute; left: 0; top: 0; width: 400px; height: 927px; background: var(--paper); }
  .side-url { position: absolute; left: 51px; top: 56px; font-size: 20px; color: var(--ink); }
  .service-title { position: absolute; left: 50px; top: 142px; font-size: 45px; line-height: 42px; }
  .service-list { position: absolute; left: 43px; top: 267px; list-style: none; font-weight: 700; font-size: 23px; }
  .service-list li { height: 60px; }
  .contact { position: absolute; left: 30px; top: 525px; }
  .contact-title { font-size: 27px; line-height: 34px; margin-bottom: 6px; }
  .contact dt { font-weight: 700; font-size: 20px; color: var(--ink-green); line-height: 30px; }
  .contact dd { font-size: 21px; line-height: 32px; margin-bottom: 6px; }

  /* central call-out */
  .callout-shape {
    position: absolute; left: 452px; top: 180px; width: 300px; height: 411px;
    background: var(--sage);
    border-top-left-radius: 160px 200px;
    border-bottom-left-radius: 40px;
  }
  .callout-text {
    position: absolute; left: 440px; top: 238px; width: 270px;
    text-align: center; font-size: 52px; line-height: 48px;
  }

  /* right info panel */
  .info-panel {
    position: absolute; left: 801px; top: 354px; width: 399px; height: 573px;
    background: var(--sage); border-top-left-radius: 80px;
  }
  .info-title { position: absolute; left: 853px; top: 452px; font-size: 29px; line-height: 33px; }
  .info-body {
    position: absolute; left: 853px; top: 524px; width: 330px;
    font-size: 17.3px; line-height: 21.6px; color: var(--ink);
  }

  /* photo placeholders */
  .photo-stage {
    position: absolute; left: 852px; top: -10px; width: 360px; height: 457px;
    border-bottom-left-radius: 190px 230px;
    border-bottom-right-radius: 120px 160px;
    background: linear-gradient(160deg, var(--photo-cool-a), var(--photo-cool-b) 55%, var(--photo-cool-c));
  }
  .photo-hall {
    position: absolute; left: 312px; top: 477px; width: 396px; height: 500px;
    border-radius: 50%;
    background: linear-gradient(200deg, var(--photo-warm-b), var(--photo-warm-a) 50%, var(--photo-warm-c));
  }

  /* brand mark */
  .brand {
    position: absolute; left: 60px; top: 717px; width: 342px; height: 201px;
    background: var(--paper);
    display: flex; align-items: center; justify-content: center; gap: 14px;
  }
  .brand-square { width: 22px; height: 22px; background: var(--ink-green); }
  .brand-name { font-weight: 700; font-size: 40px; color: var(--ink-green); }
</style>
</head>
<body>
<main class="flyer">
  <aside class="side-panel">
    <p class="side-url">www.holzlounge-verleih.de</p>
    <h2 class="service-title display">Unser<br>Service</h2>
    <ul class="service-list">
      <li>Verkauf</li>
      <li>Vermietung</li>
      <li>Anlieferung</li>
    </ul>
    <section class="contact">
      <h3 class="contact-title display">Kontakt:</h3>
      <dl>
        <dt>Phone</dt>
        <dd>0170 5550148</dd>
        <dt>Website</dt>
        <dd>www.holzlounge-verleih.de</dd>
      </dl>
    </section>
  </aside>

  <div class="callout-shape"></div>
  <h1 class="callout-text display">Kontak<br>tieren<br>Sie uns<br>jetzt!</h1>

  <div class="photo-stage" role="img" aria-label="Eventsaal mit Bühne in violettem Licht, Palettentische mit roten Sitzkissen und Kerzenleuchtern"></div>

  <section class="info-panel"></section>
  <h2 class="info-title display">Wieso<br>Palettenmöbel?</h2>
  <p class="info-body">Unsere Palettenmöbel sind das neuste Highlight in unserem Online-Shop. Sie zeichnen sich durch Einzigartigkeit, modernen Stil und absolut robustes Holz aus. Erfreuen sie sich an diesen Möbelstücken und erleben Sie die "Individualität" dieses kostbaren Möbelstückes. Lange wurden Paletten für harte Arbeit genutzt. Heute ist es getreu dem Upcyling-Trend für moderne Menschen und aus exklusiven Wohnräumen nicht mehr wegzudenken!</p>

  <div class="photo-hall" role="img" aria-label="Backsteinhalle mit Rundbogenfenstern, bunt beleuchtet, eingerichtet mit Palettensesseln und Stehtischen"></div>

  <div class="brand">
    <span class="brand-square"></span>
    <span class="brand-name">Holzlounge</span>
  </div>
</main>
</body>
</html>
```